40k Ultra High Pressure Waterblasting Ad

Clean, Simple, To the point. We need an ad for our industry magazine. Our company Brook Spray Systems, Inc. caters to contractors in the Utra High Pressure Waterblasting Industry. We manufacture in house a majority of the items we sell. We'd like the ad to imply that we believe in good customer service, building relationships with our customers and going above and beyond to meet our customer needs. Our main products we sell are our Quartzline Tips and Dorven Mallory Hoses. Our website is Brookspray.example for images of our products.

Attached are some of our previous ads we've made.

I like the icons we used in the "Dorven ad" listing some of our keys products we sell.

Target Market(s)

Contractors

Industry/Entity Type

Industry

Colors

Designer to choose colors to be used in the design.

Requirements
Must have
• At least 1 item we sell

```html
<!DOCTYPE html>
<html lang="en">
<head>
<meta charset="utf-8">
<title>Brook Spray Systems – UHP Surface Preparation Ad</title>
<link href="https://fonts.googleapis.com/css2?family=Open+Sans:wght@400;600;700&family=Roboto+Condensed:wght@700&display=swap" rel="stylesheet">
<style>
:root{
  --stage:#3b3b3b;
  --paper:#f7f8fb;
  --navy:#1c237f;
  --royal:#2626a3;
  --blue:#1f6cc0;
  --sky:#3d8fe0;
  --ice:#dfe8f4;
  --ink:#1d2b4f;
  --white:#ffffff;
}
*{margin:0;padding:0;box-sizing:border-box}
html,body{width:1200px;height:1200px;overflow:hidden;background:var(--stage)}
.ad{position:absolute;left:210px;top:48px;width:780px;height:1104px;background:var(--paper);overflow:hidden;font-family:"Open Sans",Arial,sans-serif;box-shadow:0 18px 40px rgba(0,0,0,.45)}
.ad__backdrop{position:absolute;left:0;top:0;width:780px;height:560px;background:linear-gradient(180deg,#d4d8de 0%,#e6e9ee 55%,rgba(247,248,251,0) 100%)}
.ad__ring{position:absolute;left:0;top:0}
.brand{position:absolute;top:52px;left:0;width:780px;display:flex;justify-content:center;align-items:center;gap:10px}
.brand__dot{width:22px;height:22px;border-radius:50%;background:var(--blue)}
.brand__name{font-family:"Roboto Condensed",Arial,sans-serif;font-weight:700;font-size:40px;color:var(--navy);letter-spacing:.5px}
.ad__product{position:absolute;left:135px;top:125px;width:430px;height:305px;border-radius:24px;background:radial-gradient(ellipse at 55% 45%,#5a5f66 0%,#8c929a 45%,#c9cdd3 75%,rgba(255,255,255,0) 100%)}
.headline{position:absolute;top:440px;left:0;width:780px;text-align:center}
.headline__lead{font-family:"Open Sans",Arial,sans-serif;font-weight:700;font-size:50px;color:var(--blue);line-height:1.1}
.headline__main{font-family:"Roboto Condensed",Arial,sans-serif;font-weight:700;font-size:68px;color:var(--blue);line-height:1.05;margin-top:4px}
.headline__sub{font-family:"Roboto Condensed",Arial,sans-serif;font-weight:700;font-size:52px;color:var(--navy);line-height:1.1}
.headline__sub span{color:var(--blue)}
.tagline{position:absolute;left:145px;top:660px;width:488px;height:42px;background:var(--royal);color:var(--white);font-size:29px;line-height:42px;text-align:center}
.features{position:absolute;top:735px;left:78px;width:640px;display:flex}
.features__col{list-style:none;font-size:15px;color:var(--ink);line-height:1.3}
.features__col li{position:relative;padding-left:22px;margin-bottom:10px}
.features__col li::before{content:"";position:absolute;left:2px;top:6px;width:9px;height:9px;border-radius:50%;background:var(--navy)}
.features__col--left{width:305px;padding-right:16px;border-right:1.5px solid #b9c3d4}
.features__col--right{padding-left:18px}
.products{position:absolute;top:868px;left:0;width:780px;height:125px}
.product{position:absolute;top:0;width:102px;height:125px}
.product__disc{width:102px;height:102px;border-radius:50%;border:3px solid var(--white);border-top-color:var(--blue);box-shadow:0 0 0 2px var(--navy) inset;background:radial-gradient(circle at 50% 50%,#6b7280 0%,#a7adb6 50%,#eef1f5 80%)}
.product__fade{position:absolute;left:6px;top:52px;width:90px;height:70px;background:linear-gradient(180deg,rgba(210,215,228,.6),rgba(247,248,251,0));z-index:-1}
.footer{position:absolute;left:0;bottom:0;width:780px;height:110px}
.footer__contact{position:absolute;left:75px;bottom:28px;font-family:"Roboto Condensed",Arial,sans-serif;font-weight:700;font-size:15px;color:var(--white);line-height:1.3;white-space:nowrap}
.footer__rule{position:absolute;left:302px;bottom:22px;width:1.5px;height:44px;background:var(--white)}
.footer__web{position:absolute;left:320px;bottom:36px;font-family:"Roboto Condensed",Arial,sans-serif;font-weight:700;font-size:15px;color:var(--white);white-space:nowrap}
</style>
</head>
<body>
<article class="ad">
  <div class="ad__backdrop" role="img" aria-label="Faded photo of an industrial plant skyline"></div>
  <svg class="ad__ring" width="780" height="560" viewBox="0 0 780 560" aria-hidden="true">
    <circle cx="405" cy="20" r="312" fill="none" stroke="var(--sky)" stroke-width="6"/>
    <circle cx="400" cy="18" r="295" fill="var(--white)" stroke="var(--navy)" stroke-width="18"/>
  </svg>
  <div class="brand"><span class="brand__dot"></span><span class="brand__name">Brook Spray</span></div>
  <div class="ad__product" role="img" aria-label="Photo of a trailer-mounted ultra high pressure waterblasting pump unit"></div>

  <header class="headline">
    <p class="headline__lead">supplying the essentials</p>
    <h1 class="headline__main">IN THE UHP SURFACE</h1>
    <p class="headline__sub">PREPARATION <span>INDUSTRY</span></p>
  </header>

  <p class="tagline">Family owned and operated</p>

  <section class="features">
    <ul class="features__col features__col--left">
      <li>couplers and fittings</li>
      <li>pneumatically driven rotating jetlance</li>
      <li>numerous types of heat treated Quartzline tips</li>
    </ul>
    <ul class="features__col features__col--right">
      <li>variety of pump replacement parts</li>
      <li>distributor of Dorven Mallory hoses</li>
    </ul>
  </section>

  <section class="products">
    <div class="product" style="left:74px"><div class="product__disc" role="img" aria-label="Photo of a rotating jetlance tool"></div><div class="product__fade"></div></div>
    <div class="product" style="left:213px"><div class="product__disc" role="img" aria-label="Photo of brass couplers and fittings"></div><div class="product__fade"></div></div>
    <div class="product" style="left:349px"><div class="product__disc" role="img" aria-label="Photo of braided high pressure hose"></div><div class="product__fade"></div></div>
    <div class="product" style="left:484px"><div class="product__disc" role="img" aria-label="Photo of black hydraulic hose coil"></div><div class="product__fade"></div></div>
    <div class="product" style="left:613px"><div class="product__disc" role="img" aria-label="Photo of black hose with fitting end"></div><div class="product__fade"></div></div>
  </section>

  <footer class="footer">
    <svg width="780" height="110" viewBox="0 0 780 110" aria-hidden="true">
      <path d="M0 10 H420 C445 10 440 28 465 28 H780 V110 H0 Z" fill="var(--blue)"/>
      <path d="M420 10 C445 10 440 28 465 28 H780" fill="none" stroke="var(--navy)" stroke-width="3"/>
    </svg>
    <p class="footer__contact">Email: info@brookspray.example<br>Phone: 555-014-2290</p>
    <span class="footer__rule"></span>
    <p class="footer__web">www.brookspray.example</p>
  </footer>
</article>
</body>
</html>
```